Copper Kettle Auctions business card design with existing logo

Looking for a sleek and sexy design using our current logo

Contact Information for Business Card

Name, address, email, phone, website. Marcus Delvane 482 Brambleton Road Suite 210C Fernbrook NY 11907 Copperkettlebids.net (948)555-0174

```html
<!DOCTYPE html>
<html lang="en">
<head>
<meta charset="utf-8">
<title>Copper Kettle Auctions – Business Card</title>
<link href="https://fonts.googleapis.com/css2?family=Open+Sans:wght@400;700&display=swap" rel="stylesheet">
<style>
  :root {
    --backdrop: #2b2b2d;
    --card: #f1f1f2;
    --navy: #2b3f86;
    --navy-dark: #1f3274;
    --red: #d32a2f;
    --white: #ffffff;
  }
  * { margin: 0; padding: 0; box-sizing: border-box; }
  html, body { width: 1200px; height: 1000px; overflow: hidden; }
  body {
    background: var(--backdrop);
    font-family: "Open Sans", Arial, sans-serif;
    position: relative;
  }
  .card {
    position: absolute;
    left: 372px;
    width: 479px;
    height: 283px;
    border-radius: 20px;
    background: var(--card);
    overflow: hidden;
    box-shadow: 0 4px 14px rgba(0,0,0,0.35);
  }
  .card--front { top: 172px; }
  .card--back { top: 550px; }

  .brand {
    position: absolute;
    display: flex;
    flex-direction: column;
    align-items: center;
    gap: 10px;
    transform: translate(-50%, -50%);
  }
  .brand__dot {
    width: 46px; height: 46px;
    border-radius: 50%;
    background: var(--red);
  }
  .brand__name {
    font-weight: 700;
    color: var(--navy-dark);
    white-space: nowrap;
    text-align: center;
    letter-spacing: 1px;
    line-height: 1.15;
  }
  .card--front .brand { left: 50%; top: 50%; }
  .card--front .brand__name { font-size: 17px; }
  .card--back .brand { left: 361px; top: 136px; gap: 8px; }
  .card--back .brand__dot { width: 38px; height: 38px; }
  .card--back .brand__name { font-size: 14px; }

  .contact-panel {
    position: absolute;
    left: 0; top: 0;
    width: 240px; height: 100%;
    background: var(--navy);
    color: var(--white);
    padding: 80px 0 0 45px;
  }
  .contact-panel__name {
    font-size: 18px;
    font-weight: 400;
    margin-bottom: 14px;
  }
  .contact-list { list-style: none; }
  .contact-list li {
    display: flex;
    align-items: flex-start;
    gap: 7px;
    font-size: 12.5px;
    line-height: 22px;
    white-space: nowrap;
  }
  .contact-list svg { flex: none; margin-top: 4px; }
  .contact-list .address span { display: block; }
  .contact-list .address span + span { padding-left: 3px; }

  .social {
    position: absolute;
    right: 34px;
    bottom: 22px;
    display: flex;
    gap: 4px;
  }
  .social span {
    width: 15px; height: 15px;
    border-radius: 50%;
    background: var(--navy-dark);
  }
</style>
</head>
<body>

<section class="card card--front">
  <div class="brand">
    <div class="brand__dot"></div>
    <div class="brand__name">COPPER KETTLE<br>AUCTIONS</div>
  </div>
</section>

<section class="card card--back">
  <div class="contact-panel">
    <h1 class="contact-panel__name">Marcus Delvane</h1>
    <ul class="contact-list">
      <li>
        <svg width="15" height="15" viewBox="0 0 15 15" aria-hidden="true">
          <rect width="15" height="15" rx="2" fill="#fff"/>
          <path d="M5 3.2l1.6 2.3-1 1c.6 1.3 1.6 2.3 2.9 2.9l1-1 2.3 1.6-.8 1.6c-3.6-.2-6.6-3.2-6.8-6.8z" fill="#2b3f86"/>
        </svg>
        (948)555-0174
      </li>
      <li>
        <svg width="15" height="15" viewBox="0 0 15 15" aria-hidden="true">
          <rect width="15" height="15" rx="2" fill="#fff"/>
          <rect x="3" y="4.5" width="9" height="6.5" fill="none" stroke="#2b3f86" stroke-width="1.2"/>
          <path d="M3 4.8l4.5 3.4 4.5-3.4" fill="none" stroke="#2b3f86" stroke-width="1.2"/>
        </svg>
        youremail@mailbox.com
      </li>
      <li>
        <svg width="15" height="15" viewBox="0 0 15 15" aria-hidden="true">
          <rect width="15" height="15" rx="2" fill="#fff"/>
          <circle cx="7.5" cy="7.5" r="4.5" fill="none" stroke="#2b3f86" stroke-width="1"/>
          <ellipse cx="7.5" cy="7.5" rx="2" ry="4.5" fill="none" stroke="#2b3f86" stroke-width="1"/>
          <path d="M3 7.5h9" stroke="#2b3f86" stroke-width="1"/>
        </svg>
        Copperkettlebids.net
      </li>
      <li>
        <svg width="15" height="15" viewBox="0 0 15 15" aria-hidden="true">
          <rect width="15" height="15" rx="2" fill="#fff"/>
          <path d="M7.5 12.5s-3.5-3.7-3.5-6a3.5 3.5 0 017 0c0 2.3-3.5 6-3.5 6z" fill="#2b3f86"/>
          <circle cx="7.5" cy="6.4" r="1.3" fill="#fff"/>
        </svg>
        <div class="address">
          <span>482 Brambleton Road Suite</span>
          <span>210C Fernbrook NY 11907</span>
        </div>
      </li>
    </ul>
  </div>

  <div class="brand">
    <div class="brand__dot"></div>
    <div class="brand__name">COPPER KETTLE<br>AUCTIONS</div>
  </div>

  <div class="social" aria-label="Social media links">
    <span></span><span></span><span></span><span></span>
  </div>
</section>

</body>
</html>
```